Business Card

Please design a business card with our logo on a cream coloured background and include the following information:

Tallowmere Shopping Centre
ph (08) 9341 7086

sales@velvetpetalblooms.com

www.velvetpetalblooms.com

on reverse:

Find us on Friendloop
friendloop.com/velvetpetalblooms

```html
<!DOCTYPE html>
<html lang="en">
<head>
<meta charset="utf-8">
<title>Velvet Petal Blooms – Business Card</title>
<link href="https://fonts.googleapis.com/css2?family=Asap:wght@400;500&family=Asap+Condensed:wght@500&display=swap" rel="stylesheet">
<style>
  :root {
    --backdrop: #262626;
    --leaf-green: #5f8a3a;
    --leaf-green-dark: #4f7a2e;
    --leaf-green-light: #6a9640;
    --cream: #efe6cf;
    --cream-dark: #e6dabd;
    --ink: #3f3f3e;
    --white: #f4f4ee;
  }
  * { margin: 0; padding: 0; box-sizing: border-box; }
  html, body {
    width: 1200px;
    height: 896px;
    overflow: hidden;
    background: var(--backdrop);
    font-family: "Asap", "Helvetica Neue", Arial, sans-serif;
  }
  .canvas { position: relative; width: 1200px; height: 896px; }

  .card {
    position: absolute;
    top: 180px;
    width: 297px;
    height: 535px;
    text-align: center;
    white-space: nowrap;
  }

  /* Reverse side */
  .card--reverse {
    left: 281px;
    background: linear-gradient(180deg, var(--leaf-green-light) 0%, var(--leaf-green) 45%, var(--leaf-green-dark) 100%);
    color: var(--white);
  }
  .reverse-name {
    position: absolute;
    top: 126px;
    left: 0;
    width: 100%;
    font-family: "Asap Condensed", "Arial Narrow", sans-serif;
    font-weight: 500;
    font-size: 30px;
    color: var(--white);
  }
  .social-heading {
    position: absolute;
    top: 412px;
    left: 0;
    width: 100%;
    font-size: 17px;
  }
  .social-link {
    position: absolute;
    top: 439px;
    left: 0;
    width: 100%;
    font-size: 15.5px;
  }

  /* Front side */
  .card--front {
    left: 628px;
    background: linear-gradient(180deg, var(--cream) 0%, var(--cream-dark) 100%);
    color: var(--ink);
  }
  .brand-mark {
    position: absolute;
    top: 66px;
    left: 123px;
    width: 50px;
    height: 50px;
    border-radius: 50%;
    background: var(--leaf-green-light);
  }
  .brand-name {
    position: absolute;
    top: 126px;
    left: 0;
    width: 100%;
    font-family: "Asap Condensed", "Arial Narrow", sans-serif;
    font-weight: 500;
    font-size: 30px;
    color: var(--ink);
  }
  .location {
    position: absolute;
    top: 239px;
    left: 0;
    width: 100%;
    font-size: 16.5px;
    letter-spacing: 0.4px;
    text-transform: uppercase;
  }
  .divider {
    position: absolute;
    left: 35px;
    width: 227px;
    height: 24px;
  }
  .divider::before, .divider::after {
    content: "";
    position: absolute;
    top: 11px;
    width: 92px;
    height: 1.5px;
    background: var(--leaf-green);
  }
  .divider::before { left: 0; }
  .divider::after { right: 0; }
  .divider svg {
    position: absolute;
    left: 102px;
    top: 0;
    width: 24px;
    height: 24px;
  }
  .divider--phone { top: 283px; }
  .divider--mail { top: 352px; }
  .divider--web { top: 421px; }
  .contact-line {
    position: absolute;
    left: 0;
    width: 100%;
    font-size: 16px;
  }
  .contact-line--phone { top: 319px; }
  .contact-line--mail { top: 387px; }
  .contact-line--web { top: 456px; }
</style>
</head>
<body>
<main class="canvas">

  <section class="card card--reverse" aria-label="Business card reverse">
    <p class="reverse-name">Velvet Petal Blooms</p>
    <p class="social-heading">Find us on Friendloop</p>
    <p class="social-link">friendloop.com/velvetpetalblooms</p>
  </section>

  <section class="card card--front" aria-label="Business card front">
    <span class="brand-mark" aria-hidden="true"></span>
    <h1 class="brand-name">Velvet Petal Blooms</h1>
    <p class="location">Tallowmere Shopping Centre</p>

    <div class="divider divider--phone">
      <svg viewBox="0 0 24 24" aria-hidden="true">
        <circle cx="12" cy="12" r="11" fill="var(--leaf-green)"/>
        <path d="M8.6 6.8c.4-.3.9-.2 1.1.2l1 1.8c.2.4.1.8-.2 1.1l-.7.6c.5 1.2 1.5 2.3 2.7 2.9l.6-.7c.3-.3.8-.4 1.1-.2l1.8 1c.4.2.5.7.2 1.1l-.8 1c-.4.5-1.1.7-1.700.5-2.9-.9-5.2-3.2-6.1-6.1-.2-.6 0-1.3.5-1.7z" fill="var(--cream)"/>
      </svg>
    </div>
    <p class="contact-line contact-line--phone">(08) 9341 7086</p>

    <div class="divider divider--mail">
      <svg viewBox="0 0 24 24" aria-hidden="true">
        <circle cx="12" cy="12" r="11" fill="var(--leaf-green)"/>
        <rect x="6.5" y="8" width="11" height="8" rx="0.8" fill="var(--cream)"/>
        <path d="M6.8 8.4 12 12.6l5.2-4.2" fill="none" stroke="var(--leaf-green)" stroke-width="1.1"/>
      </svg>
    </div>
    <p class="contact-line contact-line--mail">sales@velvetpetalblooms.com</p>

    <div class="divider divider--web">
      <svg viewBox="0 0 24 24" aria-hidden="true">
        <circle cx="12" cy="12" r="11" fill="var(--leaf-green)"/>
        <path d="M12 5.8a4 4 0 0 0-4 4c0 3 4 8 4 8s4-5 4-8a4 4 0 0 0-4-4z" fill="var(--cream)"/>
        <circle cx="12" cy="9.8" r="1.5" fill="var(--leaf-green)"/>
      </svg>
    </div>
    <p class="contact-line contact-line--web">www.velvetpetalblooms.com</p>
  </section>

</main>
</body>
</html>
```